Harborlight Venture Studio (HVS)

Create a Flyer similar to the example or better

Target Market(s)

Management of Corporate Companies

Requirements
Must have
• follow the PDF-example
Nice to have
• compelling

```html
<!DOCTYPE html>
<html lang="en">
<head>
<meta charset="utf-8">
<title>Harborlight Venture Studio – Retreat Flyer</title>
<link href="https://fonts.googleapis.com/css2?family=Montserrat:wght@300;400;500;600&display=swap" rel="stylesheet">
<style>
  :root{
    --navy:#15183f;
    --ink:#1c2150;
    --sea-deep:#14233b;
    --sea-mid:#1f3a55;
    --sea-light:#2f5470;
    --gold-dark:#a98a2e;
    --gold:#e2bb45;
    --gold-bright:#f3cd4f;
    --text:#ffffff;
  }
  *{margin:0;padding:0;box-sizing:border-box}
  html,body{width:1200px;height:848px;overflow:hidden;background:var(--navy)}
  .flyer{position:relative;width:1200px;height:848px;overflow:hidden;font-family:"Montserrat",sans-serif;color:var(--text)}
  .sea-photo{position:absolute;left:0;top:0;width:796px;height:848px;
    background:radial-gradient(ellipse at 35% 45%,var(--sea-light) 0%,transparent 55%),
               linear-gradient(160deg,var(--sea-mid) 0%,var(--sea-deep) 60%,#101c33 100%)}
  .side-panel{position:absolute;left:796px;top:0;width:404px;height:848px;background:var(--navy)}
  .shapes{position:absolute;left:0;top:0;width:1200px;height:848px}
  .block{position:absolute;font-weight:300;font-size:9.4px;line-height:13.9px;letter-spacing:-0.05px}
  .block p{text-align:justify;margin-bottom:11px}
  .block p.plain{text-align:left}
  .block p.indent{padding-left:122px;margin-bottom:4px}
  h2{font-weight:500;font-size:18px;line-height:31px;margin-bottom:12px;letter-spacing:0}
  h2.light{font-weight:400;font-size:16.2px;line-height:22px;margin-bottom:14px}
  .day{position:absolute;font-weight:600;font-size:16px;color:var(--ink)}
</style>
</head>
<body>
<div class="flyer">
  <div class="sea-photo" role="img" aria-label="Aerial photograph of surfers riding deep blue ocean waves"></div>
  <div class="side-panel"></div>

  <svg class="shapes" viewBox="0 0 1500 1060" preserveAspectRatio="none" aria-hidden="true">
    <defs>
      <linearGradient id="ribbon" x1="0" x2="1" y1="0" y2="0">
        <stop offset="0" stop-color="var(--gold-dark)"/>
        <stop offset="0.35" stop-color="var(--gold)"/>
        <stop offset="1" stop-color="var(--gold-bright)"/>
      </linearGradient>
      <linearGradient id="sweep" x1="0" x2="1" y1="0" y2="0">
        <stop offset="0" stop-color="var(--gold-dark)"/>
        <stop offset="1" stop-color="var(--gold-bright)"/>
      </linearGradient>
    </defs>
    <path d="M995,60 C1180,35 1380,40 1500,225 L1500,0 L1330,0 C1200,18 1080,40 995,60 Z" fill="url(#sweep)"/>
    <path d="M520,790 C720,770 900,760 990,800 C1050,860 1080,960 1170,1005 C1260,1045 1400,1045 1500,1060 L930,1060 C1000,1000 1010,880 960,830 C880,800 700,795 520,790 Z" fill="url(#sweep)"/>
    <path d="M930,1060 C1000,1000 1010,880 960,830 C1010,870 1030,980 1000,1060 Z" fill="var(--navy)"/>
    <path d="M512,4 C680,22 840,30 995,60 C830,46 680,58 512,78 Z" fill="url(#ribbon)"/>
    <path d="M515,252 C690,270 860,280 992,310 C850,300 690,315 515,330 Z" fill="url(#ribbon)"/>
    <path d="M512,430 C690,446 860,456 988,488 C850,480 690,492 512,506 Z" fill="url(#ribbon)"/>
    <path d="M512,612 C690,628 860,640 988,670 C850,662 690,675 512,690 Z" fill="url(#ribbon)"/>
    <path d="M0,712 C200,728 420,770 620,784 C780,794 900,795 1000,800 C820,804 560,800 0,805 Z" fill="url(#ribbon)"/>
  </svg>

  <div class="day" style="left:446px;top:26px">Day 2</div>
  <div class="day" style="left:446px;top:227px">Day 3</div>
  <div class="day" style="left:446px;top:368px">Day 4</div>
  <div class="day" style="left:446px;top:514px">Day 5</div>
  <div class="day" style="left:44px;top:608px">Day 1</div>

  <section class="block" style="left:43px;top:46px;width:336px">
    <h2>Our local infrastructure for this retreat (The Masseria)</h2>
    <p>The Masseria (and Italian off-side estate) offers space for up to 10 innovators within the lovely and healthy environment of Apulia representing a totally refurbished, climatized and perfectly maintained first-class hospitality. The area also offers sufficient space for distraction and collection of thoughts, ideas and profound innovations. The intermediate HVS process steps will situationally be conducted either inside the climatized meeting rooms or on the covered country yard – or even in the form of focused off-side interventions in the open nature. The…</p>
  </section>

  <section class="block" style="left:43px;top:264px;width:336px">
    <h2 style="line-height:23px;margin-bottom:22px">How you can tailor your individual HVS process</h2>
    <p>During the preparation of this retreat we<br>are able to tailor the complete process to your specific needs and individualized requirements. All accommodation and dining (breakfast, lunch and dinner buffet) for the time of your innovator's stay with us is covered and ensured. Your innovators will be fully covered by a specific event-insurance.</p>
  </section>

  <section class="block" style="left:43px;top:437px;width:336px">
    <h2 style="margin-bottom:8px">The investment</h2>
    <p>As the complete process, content wise, can and will be tailored to your specific needs and expectations there is no unique price tag attached to it. Nevertheless, here is an indication of a cost tag for the HVS process (based on the Arc Method): €12.000 – €15.000 (excl. VAT) per person / 5-days. This indication has to be understood as the price including all services from the Departure Airport Sorvello-International and back.</p>
  </section>

  <section class="block" style="left:44px;top:654px;width:340px">
    <p class="plain" style="margin-bottom:13px">Downloading pattern from the past (9 hours)</p>
    <p class="plain" style="margin-bottom:13px">The focus of our work today, is your current situation in the context, which we defined for this particular 5 day HVS process.</p>
    <p class="indent" style="margin-bottom:13px">Suspending</p>
    <p class="plain" style="margin-bottom:13px">Finding and applying options and opportunities to overcome your company's traditional thinking and collaboration attitude.</p>
    <p class="indent">Re-Directing</p>
    <p class="indent">Letting Go</p>
  </section>

  <section class="block" style="left:444px;top:81px;width:314px">
    <p class="plain">Presencing and identification of the organization's blind spots (12 hours)</p>
    <p>The focus of our work today are questions and tasks around the purpose and sense of your current processes, attitudes and the organization's contributors. Identifying the blind spots by answering questions such as "Who is myself in the process?" and "What is my work and responsibility – on the whole".</p>
  </section>
  <section class="block" style="left:444px;top:278px;width:318px">
    <p class="plain">Letting the options come and crystallization of valuable solutions (12 hours)</p>
  </section>
  <section class="block" style="left:444px;top:422px;width:318px">
    <p class="plain">Crystallization, concretization &amp; prototyping – How might we.. (12 hours)</p>
  </section>
  <section class="block" style="left:444px;top:560px;width:318px">
    <p class="plain">Developing prototypes for processes and innovations &amp; Initiation of performing (How to get the job done…) (8 hours)</p>
  </section>
  <section class="block" style="left:444px;top:653px;width:314px">
    <p style="margin-bottom:13px">Around 16:30 the shuttle service will be waiting to transport the innovators back to Sorvello-International-Airport. Our staff will guide your innovators back to the Airport the journey stared. From here your organization will have the chance and challenge to reflect, to adopt and to implement the working results of your innovators.</p>
    <p>The HVS process conducted during this retreat covers in total more than 50 hours of intense refection, extraction and intervention time – so the results will be profound and, once implemented, your business will be enabled toward the next level of efficiency and performance.</p>
  </section>

  <section class="block" style="left:842px;top:126px;width:321px">
    <h2 class="light">Set-up, preparation and execution…</h2>
    <p>Our Harborlight Venture Studio (HVS) process follows the principals of the Arc Method approach and is based on application of Agile principals and methodologies of Design Thinking and SCRUM. The aim of the HVS process is to enable your corporate organization to anticipate the requirements of the era of "Disruptive Innovation". (1.) Our joint journey starts with the assessment of your organization's best brains – jointly we prepare your specific content and process targets – and we will integrate them into our given structure. (2.) We enable your eligible contributors with tools and methodologies – to succeed successfully with the process. (3.) During the process with facilitation at our estate in Italy, your organization's contributors will apply their technical and business competence in accordance with the principals of the HVS process. (4.) In teams, (amount to be defined) your organization's contributors are guided through the Arc process – and the innovation and creation of innovative and feasible business concepts are almost guaranteed. (5) After the completion of the HVS process, your facilitators (if you wish), with Northmere Consulting &amp; Coaching LLC support, will ensure the implementation of the elaborated innovation in the context of your corporate organization. Important: Our aim is to enable your organization to innovate on demand – we support you in the execution and the preparation of related steps on demand – and at your request</p>
  </section>

  <section class="block" style="left:842px;top:538px;width:321px">
    <h2 class="light">How the HVS process will be conducted…</h2>
    <p>Together with your chosen management staff (your innovators) you will retreat to our pre-configured facility in Italy. We shall pick up the innovators at the import of your choice and fly with them to the international airport of Sorvello (I). From Sorvello-Airport we will guide and accompany the innovators via our shuttle service to our first-class maintained Masseria (the retreat). We will arrive there at around 10.00 a.m. After a brief welcome our process will start at around 11.00 a.m. with the first step of the Arc-Process:</p>
  </section>
</div>
</body>
</html>
```